Wedding Program

Miriam and Owen are getting married. They are looking for a simple 4-page program that conveys the special day. Venue is a museum in a large East-Coast city: classic 18th century, formal. Ceremony is non-religious. Party includes a photo booth and DJ.

He's a math geek - she's an activist/educator.

Please incorporate unique design sensibility - be creative! Colors of purple, eggplant, ivory, and gray are the couple's choice. Fall motif OK.

Target Market(s)

ages 25 - 85, members of a family

Industry/Entity Type

Graphic Design

Font styles to use
Serif
Decorative

Colors
8769ae
b7a5cd
fece3e
f78f20
757575
cfcfcf
6b449b
a64599
fffaee

Requirements
Must have
• Readable, attractive 4-color design using the copy and image provided in the attachment.
Nice to have
• It's a LOVE-ly day for a wedding - be creative!
Should not have
• Avoid flowery girly-girl fonts or obvious hearts and flowers stuff.

```html
<!DOCTYPE html>
<html lang="en">
<head>
<meta charset="utf-8">
<title>The Marriage Celebration of Miriam Hartley &amp; Owen Delmar</title>
<link rel="stylesheet" href="https://fonts.googleapis.com/css2?family=Cinzel:wght@400&family=EB+Garamond:ital,wght@0,700;1,400&family=Share+Tech+Mono&display=swap">
<style>
  :root {
    --paper: #fffaee;
    --ink: #2a2230;
    --gray: #757575;
    --silver: #cfcfcf;
    --lavender: #b7a5cd;
    --violet: #8769ae;
    --eggplant: #6b449b;
    --plum: #a64599;
    --ivory: #fffaee;
  }
  * { margin: 0; padding: 0; box-sizing: border-box; }
  html, body { width: 1200px; height: 900px; overflow: hidden; background: var(--paper); }
  .program { position: relative; width: 1200px; height: 900px; color: var(--ink); }

  .display { font-family: "Cinzel", "Times New Roman", serif; font-weight: 400; text-align: center; line-height: 50px; }
  .verse { font-family: "EB Garamond", Georgia, serif; font-style: italic; font-size: 18px; line-height: 24.5px; text-align: center; }

  /* Inside page */
  .guests-banner {
    position: absolute; left: 48px; top: 119px; width: 543px; height: 116px;
    background: var(--lavender); color: var(--ivory); font-size: 42px; padding-top: 8px;
  }
  .welcome { position: absolute; left: 48px; width: 543px; }
  .welcome-top { top: 254px; }
  .welcome-bottom { top: 628px; }
  .welcome p + p { margin-top: 24.5px; }
  .photo-spot {
    position: absolute; left: 48px; width: 543px; top: 500px;
    font-family: "EB Garamond", Georgia, serif; font-weight: 700; font-size: 31px; text-align: center;
    color: var(--eggplant);
  }

  /* Cover page */
  .bouquet { position: absolute; left: 700px; top: 28px; width: 380px; height: 340px; }
  .date { position: absolute; left: 700px; width: 380px; top: 364px; font-size: 17px; }
  .title { position: absolute; left: 700px; width: 380px; top: 385px; font-size: 42px; color: var(--eggplant); }
  .couple-band {
    position: absolute; left: 720px; top: 537px; width: 359px; height: 156px;
    background: var(--eggplant); color: var(--ivory); font-size: 37px; padding-top: 4px; line-height: 49px;
  }
  .couple-band .amp { font-family: "EB Garamond", Georgia, serif; font-weight: 700; font-size: 38px; display: block; color: var(--lavender); }
  .time {
    position: absolute; left: 700px; width: 380px; top: 725px;
    font-family: "Share Tech Mono", "Courier New", monospace; font-size: 17px; letter-spacing: 3px; text-align: center;
    color: var(--gray);
  }
  .venue { position: absolute; left: 700px; width: 380px; top: 756px; }
</style>
</head>
<body>
<main class="program">
  <section class="inside-page">
    <h2 class="guests-banner display">To our<br>Wedding Guests,</h2>
    <div class="welcome welcome-top verse">
      <p>Your presence here adds greatly<br>to our joy and happiness on this special day.</p>
      <p>Today marks the beginning of our lives together.<br>We stand before you now,<br>declaring our love for each other<br>and for our intent to be joined in marriage.</p>
    </div>
    <p class="photo-spot">wedding picture here</p>
    <div class="welcome welcome-bottom verse">
      <p>We share with each other without reservation<br>our lives, fortunes and future.</p>
      <p>We hope that you will continue to wish us well in our new life<br>and we are grateful to have your love, care and<br>best wishes for today and always!</p>
    </div>
  </section>

  <section class="cover-page">
    <svg class="bouquet" role="img" aria-label="Purple and lavender bouquet of autumn lilies and roses" viewBox="0 0 380 340">
      <defs>
        <radialGradient id="bloom" cx="50%" cy="52%" r="52%">
          <stop offset="0" stop-color="#fffaee"/>
          <stop offset="0.35" stop-color="#b7a5cd"/>
          <stop offset="0.75" stop-color="#8769ae"/>
          <stop offset="1" stop-color="#6b449b" stop-opacity="0"/>
        </radialGradient>
      </defs>
      <ellipse cx="190" cy="175" rx="185" ry="160" fill="url(#bloom)"/>
    </svg>
    <p class="date verse">Saturday, November 1, 2015</p>
    <h1 class="title display">The Marriage<br>Celebration<br>of</h1>
    <div class="couple-band display">
      Miriam Hartley
      <span class="amp">&amp;</span>
      Owen Delmar
    </div>
    <p class="time">AT 6 P.M. IN THE EVENING</p>
    <p class="venue verse">The Ashford Hall of Sciences<br>Philadelphia Pennsylvania</p>
  </section>
</main>
</body>
</html>
```